Cardiology practice business card

We need a business card for our cardiology practice "Bellmoor Cardiology". We have a new logo, attached below. We like the colours in the logo - red and charcoal. The front of the business card will need to have the doctors name, address, phone number and email. The back will need to have space to write 2 appointment dates and times.

```html
<!DOCTYPE html>
<html lang="en">
<head>
<meta charset="utf-8">
<title>Bellmoor Cardiology – Business Card</title>
<link href="https://fonts.googleapis.com/css2?family=Poppins:wght@400;500;600;700&display=swap" rel="stylesheet">
<style>
  :root {
    --red: #ec2227;
    --charcoal: #4d4e52;
    --ink: #1c1c1c;
    --rule: #bfc1c3;
    --paper: #ffffff;
    --backdrop: #d3d7d7;
  }
  * { box-sizing: border-box; margin: 0; padding: 0; }
  html, body {
    width: 1200px; height: 960px; overflow: hidden;
    background: var(--backdrop);
    font-family: "Poppins", sans-serif;
  }
  .card {
    position: absolute; left: 250px; width: 701px; height: 400px;
    background: var(--paper); border-radius: 34px; overflow: hidden;
  }
  .card--back { top: 60px; }
  .card--front { top: 500px; }
  .card__band {
    position: absolute; left: 0; right: 0; bottom: 0; height: 24px;
    background: var(--red); border-top: 2px solid var(--charcoal);
  }

  /* Appointment side */
  .appt-title {
    position: absolute; top: 20px; left: 0; right: 0; text-align: center;
    color: var(--red); font-size: 35px; font-weight: 500; letter-spacing: 0.3px;
  }
  .slot {
    position: absolute; left: 73px; width: 554px; height: 121px;
    border: 3.5px solid var(--red); border-radius: 6px; overflow: hidden;
  }
  .slot--second { top: 242px; border-color: var(--charcoal); }
  .slot--first { top: 100px; }
  .slot__days {
    display: flex; justify-content: space-between; height: 36px;
    padding: 0 17px 0 12px; align-items: center;
    background: var(--red); color: #fff; font-size: 20px; font-weight: 500;
  }
  .slot--second .slot__days { background: var(--charcoal); }
  .slot__row {
    position: absolute; left: 12px; right: 14px; display: flex; align-items: baseline;
    font-size: 20px; font-weight: 500; color: var(--ink);
  }
  .slot__row--date { top: 43px; }
  .slot__row--time { top: 80px; }
  .slot__line { flex: 1; border-bottom: 1.5px solid var(--rule); margin: 0 9px 0 9px; transform: translateY(-4px); }
  .slot__line--date { flex: 0 0 214px; }
  .slot__line--time { margin-left: 6px; margin-right: 0; }
  .slot__line--year { margin-right: 0; }

  /* Contact side */
  .brand {
    position: absolute; left: 30px; top: 158px; width: 290px;
    color: var(--red); font-size: 32px; font-weight: 600; line-height: 1.1;
    text-transform: uppercase; letter-spacing: 1px;
  }
  .bracket { position: absolute; left: 345px; top: 50px; }
  .person { position: absolute; left: 404px; top: 82px; }
  .person__name { font-size: 37px; line-height: 1; color: var(--charcoal); font-weight: 400; white-space: nowrap; }
  .person__name strong { color: var(--red); font-weight: 700; }
  .person__role { font-size: 19px; font-weight: 500; color: var(--ink); margin-top: 4px; }
  .address { position: absolute; left: 404px; top: 164px; color: var(--red); font-size: 19.5px; line-height: 26px; letter-spacing: 0.3px; }
  .contacts { position: absolute; left: 404px; top: 232px; list-style: none; }
  .contacts li { display: flex; align-items: center; height: 26px; font-size: 20px; color: var(--ink); letter-spacing: 0.3px; white-space: nowrap; }
  .contacts svg { width: 18px; height: 18px; margin-right: 11px; flex: none; }
</style>
</head>
<body>

<section class="card card--back" aria-label="Appointment side">
  <h1 class="appt-title">Appointment</h1>

  <div class="slot slot--first">
    <div class="slot__days"><span>Sun</span><span>Mon</span><span>Tue</span><span>Wed</span><span>Thr</span><span>Fri</span><span>Sat</span></div>
    <div class="slot__row slot__row--date"><span>Date/Month</span><span class="slot__line slot__line--date"></span><span>Year</span><span class="slot__line slot__line--year"></span></div>
    <div class="slot__row slot__row--time"><span>Time</span><span class="slot__line slot__line--time"></span></div>
  </div>

  <div class="slot slot--second">
    <div class="slot__days"><span>Sun</span><span>Mon</span><span>Tue</span><span>Wed</span><span>Thr</span><span>Fri</span><span>Sat</span></div>
    <div class="slot__row slot__row--date"><span>Date/Month</span><span class="slot__line slot__line--date"></span><span>Year</span><span class="slot__line slot__line--year"></span></div>
    <div class="slot__row slot__row--time"><span>Time</span><span class="slot__line slot__line--time"></span></div>
  </div>

  <div class="card__band"></div>
</section>

<section class="card card--front" aria-label="Contact side">
  <p class="brand">Bellmoor<br>Cardiology</p>

  <svg class="bracket" width="140" height="300" viewBox="0 0 140 300" aria-hidden="true">
    <path d="M132 7 H10 a5 5 0 0 0 -5 5 V288 a5 5 0 0 0 5 5 H132" fill="none" stroke="var(--red)" stroke-width="2"/>
    <circle cx="132" cy="7" r="5" fill="var(--red)"/>
    <circle cx="132" cy="293" r="5" fill="var(--red)"/>
  </svg>

  <div class="person">
    <p class="person__name"><strong>Marta</strong> Kovena</p>
    <p class="person__role">Founder &amp; CEO</p>
  </div>

  <p class="address">1840 Linden Ave. Suite 310<br>Easton, TX 76210</p>

  <ul class="contacts">
    <li>
      <svg viewBox="0 0 24 24" aria-hidden="true"><path fill="var(--red)" d="M6.6 10.8a15.1 15.1 0 0 0 6.6 6.6l2.2-2.2a1 1 0 0 1 1-.25 11.4 11.4 0 0 0 3.6.57 1 1 0 0 1 1 1V20a1 1 0 0 1-1 1A17 17 0 0 1 3 4a1 1 0 0 1 1-1h3.5a1 1 0 0 1 1 1c0 1.250.2 2.45.57 3.57a1 1 0 0 1-.25 1z"/></svg>
      (555) 412-0387
    </li>
    <li>
      <svg viewBox="0 0 24 24" aria-hidden="true"><rect x="2" y="5" width="20" height="15" rx="1.5" fill="var(--red)"/><path d="M3 6.5l9 7 9-7" fill="none" stroke="#fff" stroke-width="1.6"/></svg>
      info@bellmoor.com
    </li>
    <li>
      <svg viewBox="0 0 24 24" aria-hidden="true"><circle cx="12" cy="12" r="10" fill="var(--red)"/><path d="M2 12h20M12 2c3 3 3 17 0 20M12 2c-3 3-3 17 0 20" fill="none" stroke="#fff" stroke-width="1.3"/></svg>
      www.bellmoor.com
    </li>
  </ul>

  <div class="card__band"></div>
</section>

</body>
</html>
```